Somebody commencing retirement at age 67 and wanting a card to introduce myself

Something that depicts the activities I intend to pursue in retirement: Travel, Golf (both in Australia and internationally), wining (red) and dining and generally leading a decadent lifestyle with my wife (or by myself as appropriate).

I offer no services, but intend to have a decadent, relaxing
retirement, playing golf, drinking red wine and dining at good
restaurants!

The card needs to have a suitably designed logo that reflects the
foregoing.

Requirements
Must have
• On the front of the card, my photograph (attached and cropped as
• appropriate), my name (Carl Brimstead), my mobile phone number (+61 417
• 532 148), my email address (carl@brimstead.example.au) and my residential
• address (41 Kestrel Lane, Marlowe Heights, Western Australia 6031,
• Australia).
• The rear of the card should have my postal address (Carl Brimstead
• Post Office Box 518 Dunmore Western Australia 6947, Australia.)._

```html
<!DOCTYPE html>
<html lang="en">
<head>
<meta charset="utf-8">
<title>Carl Brimstead – Business Card</title>
<link rel="stylesheet" href="https://fonts.googleapis.com/css2?family=Roboto+Condensed:wght@400;700&display=swap">
<style>
  :root {
    --canvas: #ffffff;
    --card: #e5eef8;
    --ink: #7a7a7a;
    --shadow: rgba(0, 0, 0, 0.10);
    --ring: #d6d9dd;
    --brand: #1aa3dc;
    --photo-a: #3f6b3a;
    --photo-b: #2a3f7a;
    --ship: #cddff2;
  }
  * { margin: 0; padding: 0; box-sizing: border-box; }
  html, body { width: 1200px; height: 1200px; overflow: hidden; background: var(--canvas); }
  body { position: relative; font-family: "Roboto Condensed", "Arial Narrow", sans-serif; color: var(--ink); }

  .card {
    position: absolute;
    width: 732px;
    height: 406px;
    background: var(--card);
    border-radius: 24px;
  }
  .card::after {
    content: "";
    position: absolute;
    left: 24px; right: 24px; bottom: -26px;
    height: 26px;
    background: radial-gradient(ellipse at 50% 0%, var(--shadow), transparent 70%);
    z-index: -1;
  }
  .card--front { left: 231px; top: 148px; }
  .card--back  { left: 230px; top: 644px; }

  .brand {
    position: absolute;
    left: 40px; top: 39px;
    width: 252px; height: 108px;
    display: flex; align-items: center; gap: 12px;
  }
  .brand__square { width: 40px; height: 40px; background: var(--brand); flex: none; }
  .brand__name { font-weight: 700; font-size: 30px; color: var(--ink); white-space: nowrap; }

  .holder-name {
    position: absolute;
    left: 38px; top: 188px;
    font-size: 35px; font-weight: 700; letter-spacing: -0.2px;
  }
  .contact {
    position: absolute;
    left: 38px; top: 252px;
    font-size: 21px; line-height: 29.5px;
  }
  .contact dt { display: inline; font-weight: 700; }
  .contact dd { display: inline; }
  .contact .row { display: block; }

  .portrait {
    position: absolute;
    left: 459px; top: 41px;
    width: 234px; height: 234px;
    border-radius: 50%;
    border: 3px solid var(--ring);
    background: #f4f6f8;
    padding: 8px;
  }
  .portrait__photo {
    width: 100%; height: 100%;
    border-radius: 50%;
    background: radial-gradient(circle at 50% 40%, #d8b89a 0 22%, transparent 23%),
                linear-gradient(180deg, var(--photo-a) 0%, #5a8a4a 55%, var(--photo-b) 80%);
  }

  .ship-art {
    position: absolute;
    left: 85px; top: 40px;
    width: 560px; height: 320px;
    border-radius: 40% 40% 20% 20%;
    background: radial-gradient(ellipse at 50% 55%, var(--ship) 0%, rgba(205, 223, 242, 0.4) 55%, transparent 75%);
  }
  .postal {
    position: absolute;
    left: 0; right: 0; top: 170px;
    text-align: center;
  }
  .postal__name { font-size: 27px; font-weight: 700; line-height: 36px; }
  .postal__address { font-size: 21px; line-height: 30px; }
</style>
</head>
<body>
  <section class="card card--front">
    <div class="brand">
      <span class="brand__square"></span>
      <span class="brand__name">Fairway &amp; Vine</span>
    </div>
    <h1 class="holder-name">Carl Brimstead</h1>
    <dl class="contact">
      <div class="row"><dt>Phone.</dt> <dd>+61 417 532 148</dd></div>
      <div class="row"><dt>Email.</dt> <dd>carl@brimstead.example.au</dd></div>
      <div class="row"><dt>Residential address.</dt> <dd>41 Kestrel Lane</dd></div>
      <div class="row"><dd>Marlowe Heights, Western Australia 6031, Australia</dd></div>
    </dl>
    <div class="portrait">
      <div class="portrait__photo" role="img" aria-label="Portrait photograph of Carl Brimstead outdoors in front of greenery"></div>
    </div>
  </section>

  <section class="card card--back">
    <div class="ship-art" role="img" aria-label="Faint line illustration of a cruise ship on waves with seagulls"></div>
    <div class="postal">
      <p class="postal__name">Carl Brimstead</p>
      <p class="postal__address">Post Office Box 518 Dunmore Western Australia 6947, Australia</p>
    </div>
  </section>
</body>
</html>
```